Flyer Design

We are a new service called quilvo.co.uk (see website) This is a premium rate £1:50 per sms text advice service. I am a qualified counsellor who already runs a practice see reslandcounselling.uk and have gotten per,it's ion from CALLMERIDIAN and are registered with them for this service. Quite simply they text Q7 followed by a brief description of their personal dilemma/life or relationship concern to 64391 this is received by me and then I text back with a brief piece of guidance and feedback on their issue. So it is a text based counselling/advice service for those who want a day to day life issue dealt with in confidence,quickly and discreetly. I want the flyers to be basic with a basic and easily transferable and identifiable image like the one on my website.

Industry/Entity Type

Counsellor

```html
<!DOCTYPE html>
<html lang="en">
<head>
<meta charset="utf-8">
<title>Quilvo – Text Counselling Flyer</title>
<link rel="stylesheet" href="https://fonts.googleapis.com/css2?family=Lobster+Two:ital,wght@0,700;1,700&display=swap">
<style>
  :root {
    --cyan-light: #62f7f6;
    --cyan-mid: #4fe3f3;
    --cyan-deep: #36c6ec;
    --body-text: #4cd8ef;
    --paper: #ffffff;
    --badge-rim: #c9f7f8;
    --badge-core-top: #5fe4f6;
    --badge-core-bottom: #38b9ea;
    --fold-line: #d7dde0;
  }
  * { margin: 0; padding: 0; box-sizing: border-box; }
  html, body { width: 1200px; height: 383px; overflow: hidden; background: var(--paper); }
  .flyer {
    position: relative;
    width: 1200px;
    height: 383px;
    font-family: "Lobster Two", cursive;
    font-weight: 700;
    overflow: hidden;
  }
  .flyer-background { position: absolute; inset: 0; }
  .brand-name {
    position: absolute;
    top: 2px;
    width: 600px;
    text-align: center;
    font-size: 62px;
    color: var(--paper);
    line-height: 1.2;
  }
  .brand-name--left { left: -14px; }
  .brand-name--right { left: 614px; }
  .panel-copy {
    position: absolute;
    font-style: italic;
    color: var(--body-text);
    line-height: 31.5px;
  }
  .panel-copy--left {
    left: 36px;
    top: 140px;
    width: 330px;
    font-size: 24.5px;
  }
  .panel-copy--right {
    right: 32px;
    top: 128px;
    width: 400px;
    font-size: 21px;
    text-align: right;
    line-height: 31px;
  }
  .badge { position: absolute; width: 180px; height: 180px; }
  .badge--left { left: 386px; top: 95px; }
  .badge--right { left: 605px; top: 95px; }
  .badge-text {
    position: absolute;
    inset: 0;
    display: flex;
    flex-direction: column;
    justify-content: center;
    align-items: center;
    text-align: center;
    color: var(--paper);
  }
  .badge-text--code { font-size: 21px; line-height: 25px; }
  .badge-text--price { font-size: 29px; line-height: 34px; }
  .web-address {
    position: absolute;
    top: 332px;
    font-size: 27px;
    color: var(--paper);
  }
  .web-address--left { right: 632px; }
  .web-address--right { left: 638px; }
</style>
</head>
<body>
<main class="flyer">
  <svg class="flyer-background" width="1200" height="383" viewBox="0 0 1200 383" aria-hidden="true">
    <defs>
      <linearGradient id="top-band" x1="0" y1="0" x2="0" y2="1">
        <stop offset="0" stop-color="var(--cyan-light)"/>
        <stop offset="1" stop-color="var(--cyan-deep)"/>
      </linearGradient>
      <linearGradient id="bottom-band" x1="0" y1="0" x2="0" y2="1">
        <stop offset="0" stop-color="var(--cyan-deep)"/>
        <stop offset="1" stop-color="var(--cyan-light)"/>
      </linearGradient>
      <linearGradient id="paper-shade" x1="0" y1="0" x2="1" y2="0">
        <stop offset="0" stop-color="#ffffff"/>
        <stop offset="0.48" stop-color="#f4f6f7"/>
        <stop offset="0.5" stop-color="#eceff0"/>
        <stop offset="0.52" stop-color="#f6f8f8"/>
        <stop offset="1" stop-color="#ffffff"/>
      </linearGradient>
    </defs>
    <rect class="paper" width="1200" height="383" fill="url(#paper-shade)"/>
    <polygon class="top-band" points="0,0 1200,0 1200,91 600,70 0,91" fill="url(#top-band)"/>
    <polyline points="0,91 600,70 1200,91" fill="none" stroke="#2aa9c9" stroke-opacity="0.35" stroke-width="2"/>
    <polygon class="bottom-band" points="0,336 600,308 1200,336 1200,383 0,383" fill="url(#bottom-band)"/>
    <polyline points="0,336 600,308 1200,336" fill="none" stroke="#2aa9c9" stroke-opacity="0.35" stroke-width="2"/>
    <line class="fold" x1="600" y1="0" x2="600" y2="383" stroke="var(--fold-line)" stroke-width="1.5"/>
  </svg>

  <h1 class="brand-name brand-name--left">Quilvo</h1>
  <h2 class="brand-name brand-name--right">Quilvo</h2>

  <p class="panel-copy panel-copy--left">Is today just not your day? Text Q7 to 64391 with your problems and a professional will give you advice and support.</p>

  <div class="badge badge--left">
    <svg width="180" height="180" viewBox="-90 -90 180 180" aria-hidden="true">
      <defs>
        <rect id="burst-square-a" x="-62" y="-62" width="124" height="124"/>
        <linearGradient id="core-a" x1="0" y1="0" x2="0" y2="1">
          <stop offset="0" stop-color="var(--badge-core-top)"/>
          <stop offset="1" stop-color="var(--badge-core-bottom)"/>
        </linearGradient>
      </defs>
      <g fill="var(--badge-rim)">
        <use href="#burst-square-a" transform="rotate(0)"/><use href="#burst-square-a" transform="rotate(7.5)"/>
        <use href="#burst-square-a" transform="rotate(15)"/><use href="#burst-square-a" transform="rotate(22.5)"/>
        <use href="#burst-square-a" transform="rotate(30)"/><use href="#burst-square-a" transform="rotate(37.5)"/>
        <use href="#burst-square-a" transform="rotate(45)"/><use href="#burst-square-a" transform="rotate(52.5)"/>
        <use href="#burst-square-a" transform="rotate(60)"/><use href="#burst-square-a" transform="rotate(67.5)"/>
        <use href="#burst-square-a" transform="rotate(75)"/><use href="#burst-square-a" transform="rotate(82.5)"/>
      </g>
      <circle r="66" fill="#2a7fa0" opacity="0.55"/>
      <circle r="63" cy="1.5" fill="url(#core-a)"/>
    </svg>
    <p class="badge-text badge-text--code"><span>Text</span><span>Q7</span><span>to</span><span>64391</span></p>
  </div>

  <div class="badge badge--right">
    <svg width="180" height="180" viewBox="-90 -90 180 180" aria-hidden="true">
      <defs>
        <rect id="burst-square-b" x="-62" y="-62" width="124" height="124"/>
        <linearGradient id="core-b" x1="0" y1="0" x2="0" y2="1">
          <stop offset="0" stop-color="var(--badge-core-top)"/>
          <stop offset="1" stop-color="var(--badge-core-bottom)"/>
        </linearGradient>
      </defs>
      <g fill="var(--badge-rim)">
        <use href="#burst-square-b" transform="rotate(0)"/><use href="#burst-square-b" transform="rotate(7.5)"/>
        <use href="#burst-square-b" transform="rotate(15)"/><use href="#burst-square-b" transform="rotate(22.5)"/>
        <use href="#burst-square-b" transform="rotate(30)"/><use href="#burst-square-b" transform="rotate(37.5)"/>
        <use href="#burst-square-b" transform="rotate(45)"/><use href="#burst-square-b" transform="rotate(52.5)"/>
        <use href="#burst-square-b" transform="rotate(60)"/><use href="#burst-square-b" transform="rotate(67.5)"/>
        <use href="#burst-square-b" transform="rotate(75)"/><use href="#burst-square-b" transform="rotate(82.5)"/>
      </g>
      <circle r="66" fill="#2a7fa0" opacity="0.55"/>
      <circle r="63" cy="1.5" fill="url(#core-b)"/>
    </svg>
    <p class="badge-text badge-text--price"><span>Only</span><span>£1.50</span></p>
  </div>

  <p class="panel-copy panel-copy--right">Quilvo is a therapy service where you can text your problems or issues to a professional who will help you solve problems, talk to you, and support you through them.</p>

  <p class="web-address web-address--left">quilvo.co.uk</p>
  <p class="web-address web-address--right">quilvo.co.uk</p>
</main>
</body>
</html>
```